Business Cards for Voslin Maybury, a law firm

We changed our firm's name from "Voslin & Maybury LLP" to "Voslin Maybury", we need to update our cards with a new design. We like the overall look of the back but the front side of the cards (see attached mockup) needs a refreshed look. I also attach our current logo so you can get rid of that LLP and &. We have a new address as well (not same as on mockup).

Target Market(s)

Clients of law firm

Industry/Entity Type

Law Firm

Contact Information for Business Card

Frontsides:

Tommaso L. Voslin
Partner
Tel: (416) 555-0172 ext. 101
Fax: (647) 555-0139
Email: tvoslin@vmlegal.ca

Peter J. Maybury
Partner
Tel: (416) 555-0172 ext. 102
Fax: (647) 555-0139
Email: petermaybury@vmlegal.ca

Reid O. Fanshaw
Barrister
Tel: (416) 555-0172 ext. 104
Fax: (647) 555-0139
Email: rfanshaw@vmlegal.ca

The back side should be crimson red (see mockup) with the logo (please update it to remove the & and the LLP, you can modify it a bit to make it tasteful if need be). Our new address is

218 Harwood Ave W, Suite 307
Toronto, ON M3K 2J5

After our address, please also include our website www.vmlegal.ca

Font styles to use
Sans Serif

Colors
ec2027
ffffff
000000

Requirements
Must have
• PLEASE NOTE: our firm's colour is more of a darker/crimson red, not a vibrant red.
• The front should have space for the lawyer's name, title, phone number (with extension), fax number, and email.
• If you're going to add those yourself, the info for the frontside is in the "Business Card Details" section (three lawyers that need their own cards).
Nice to have
• We like the backside of our current cards, just update it with our new address (one address now instead of 2), and a slightly modified logo (not a new logo altogether).
• The frontside should be refreshed with a better look (think minimalist, professional and modern), although still predominantly white-based background.
Should not have
• No scales of justice or other cheesy lawyer stereotype symbols! :-)

```html
<!DOCTYPE html>
<html lang="en">
<head>
<meta charset="utf-8">
<title>Voslin Maybury – Business Cards</title>
<link rel="stylesheet" href="https://fonts.googleapis.com/css2?family=Barlow:wght@500;600;700;800&family=Montserrat:wght@400;500&display=swap">
<style>
  :root {
    --crimson: #c41d17;
    --ink: #111111;
    --white: #ffffff;
    --canvas: #f3f3f3;
    --faint: #f1f1f1;
    --rule: #dedede;
    --font-brand: "Barlow", Arial, sans-serif;
    --font-body: "Montserrat", Arial, sans-serif;
  }
  * { box-sizing: border-box; margin: 0; padding: 0; }
  html, body { width: 1200px; height: 640px; overflow: hidden; background: var(--canvas); }
  .sheet { position: relative; width: 1200px; height: 640px; }

  .card {
    position: absolute; width: 559px; height: 281px; overflow: hidden;
    background: var(--white);
    box-shadow: 0 2px 6px rgba(0,0,0,0.12);
  }
  .card--back { left: 30px; top: 27px; background: var(--crimson); box-shadow: none; }
  .card--front-a { left: 620px; top: 27px; }
  .card--front-b { left: 26px; top: 334px; }
  .card--front-c { left: 620px; top: 334px; }

  .brand { position: absolute; display: flex; flex-direction: column; align-items: center; }
  .brand__dot { width: 54px; height: 54px; border-radius: 50%; background: var(--crimson); margin-bottom: 10px; }
  .brand__name {
    font-family: var(--font-brand); font-weight: 700; font-size: 19px;
    color: var(--crimson); white-space: nowrap; line-height: 1;
  }
  .card--back .brand__dot { width: 84px; height: 84px; background: var(--white); margin-bottom: 16px; }
  .card--back .brand__name { font-size: 31px; color: var(--white); }

  .back-rule { position: absolute; left: 0; right: 0; top: 202px; height: 1.5px; background: #3a0c0a; }
  .back-address {
    position: absolute; left: 25px; top: 225px; display: flex; gap: 8px;
    font-family: var(--font-brand); font-weight: 600; font-size: 12.5px; line-height: 16px; color: var(--white);
  }
  .back-address svg { width: 16px; height: 20px; fill: #111; margin-top: 2px; }
  .back-web {
    position: absolute; right: 46px; top: 233px;
    font-family: var(--font-brand); font-weight: 600; font-size: 13px; letter-spacing: 0.5px; color: var(--white);
  }

  .divider { position: absolute; width: 2px; background: var(--rule); }
  .name-rule { position: absolute; height: 3px; background: var(--faint); }

  .person { position: absolute; }
  .person__name {
    font-family: var(--font-brand); font-weight: 800; font-size: 15.5px; letter-spacing: 0.6px;
    color: var(--ink); line-height: 18px;
  }
  .person__name--red { color: var(--crimson); }
  .person__title { font-family: var(--font-body); font-size: 13px; color: var(--crimson); line-height: 18px; }

  .contacts { position: absolute; list-style: none; }
  .contacts li {
    display: flex; align-items: center; gap: 6px;
    font-family: var(--font-body); font-size: 13px; color: #222; line-height: 17.5px;
  }
  .contacts svg { width: 11px; height: 11px; fill: var(--crimson); flex: none; }
</style>
</head>
<body>
<svg width="0" height="0" style="position:absolute" aria-hidden="true">
  <symbol id="icon-phone" viewBox="0 0 24 24"><path d="M6.6 10.8a15.2 15.2 0 0 0 6.6 6.6l2.2-2.2c.3-.3.7-.4 1-.2 1.1.4 2.3.6 3.6.6.6 0 1 .4 1 1V20c0 .6-.4 1-1 1A17 17 0 0 1 3 4c0-.6.4-1 1-1h3.5c.6 0 1 .4 1 1 0 1.3.2 2.5.6 3.6.1.3 0 .7-.2 1z"/></symbol>
  <symbol id="icon-fax" viewBox="0 0 24 24"><path d="M6 2h12v5H6z"/><path d="M3 8h18a2 2 0 0 1 2 2v7h-4v5H5v-5H1v-7a2 2 0 0 1 2-2zm4 8v4h10v-4z"/></symbol>
  <symbol id="icon-mail" viewBox="0 0 24 24"><path d="M2 5h20v14H2z" opacity=".85"/><path d="M2 5l10 8 10-8v2l-10 8L2 7z" fill="#fff"/></symbol>
  <symbol id="icon-pin" viewBox="0 0 24 30"><path d="M12 0a10 10 0 0 0-10 10c0 7.5 10 20 10 20s10-12.5 10-20A10 10 0 0 0 12 0zm0 14a4 4 0 1 1 0-8 4 4 0 0 1 0 8z"/></symbol>
</svg>

<main class="sheet">
  <!-- Back -->
  <section class="card card--back" aria-label="Card back">
    <div class="brand" style="left:0; right:0; top:38px;">
      <span class="brand__dot"></span>
      <span class="brand__name">Voslin Maybury</span>
    </div>
    <div class="back-rule"></div>
    <div class="back-address">
      <svg><use href="#icon-pin"/></svg>
      <p>218 Harwood Ave W, Suite 307<br>Toronto, ON M3K 2J5</p>
    </div>
    <p class="back-web">www.vmlegal.ca</p>
  </section>

  <!-- Front A -->
  <section class="card card--front-a" aria-label="Card front, centred layout">
    <div class="brand" style="left:43px; width:160px; top:100px;">
      <span class="brand__dot"></span>
      <span class="brand__name">Voslin Maybury</span>
    </div>
    <div class="divider" style="left:236px; top:47px; height:190px;"></div>
    <div class="person" style="left:298px; top:98px;">
      <p class="person__name">Tommaso L. Voslin</p>
      <p class="person__title">Partner</p>
    </div>
    <ul class="contacts" style="left:298px; top:158px;">
      <li><svg><use href="#icon-phone"/></svg>(416) 555-0172 ext. 101</li>
      <li><svg><use href="#icon-fax"/></svg>(647) 555-0139</li>
      <li><svg><use href="#icon-mail"/></svg>tvoslin@vmlegal.ca</li>
    </ul>
  </section>

  <!-- Front B -->
  <section class="card card--front-b" aria-label="Card front, left-aligned layout">
    <div class="brand" style="left:370px; width:164px; top:28px;">
      <span class="brand__dot"></span>
      <span class="brand__name">Voslin Maybury</span>
    </div>
    <div class="person" style="left:32px; top:112px;">
      <p class="person__name person__name--red">Tommaso L. Voslin</p>
      <p class="person__title">Partner</p>
    </div>
    <div class="name-rule" style="left:30px; top:169px; width:190px;"></div>
    <ul class="contacts" style="left:32px; top:197px;">
      <li><svg><use href="#icon-phone"/></svg>(416) 555-0172 ext. 101</li>
      <li><svg><use href="#icon-fax"/></svg>(647) 555-0139</li>
      <li><svg><use href="#icon-mail"/></svg>tvoslin@vmlegal.ca</li>
    </ul>
  </section>

  <!-- Front C -->
  <section class="card card--front-c" aria-label="Card front, divided layout">
    <div class="brand" style="left:56px; width:160px; top:98px;">
      <span class="brand__dot"></span>
      <span class="brand__name">Voslin Maybury</span>
    </div>
    <div class="divider" style="left:250px; top:46px; height:190px;"></div>
    <div class="person" style="left:313px; top:96px;">
      <p class="person__name">Tommaso L. Voslin</p>
      <p class="person__title">Partner</p>
    </div>
    <ul class="contacts" style="left:313px; top:157px;">
      <li><svg><use href="#icon-phone"/></svg>(416) 555-0172 ext. 101</li>
      <li><svg><use href="#icon-fax"/></svg>(647) 555-0139</li>
      <li><svg><use href="#icon-mail"/></svg>tvoslin@vmlegal.ca</li>
    </ul>
  </section>
</main>
</body>
</html>
```